Sterling Floorworks Letterhead

Letterhead used for business reasons. It must be editable and easy to use.

Address is 5127 W. Harbor Lane Brookfield OR 97381 - 941.382.5519

```html
<!DOCTYPE html>
<html lang="en">
<head>
<meta charset="utf-8">
<title>Sterling Floorworks Letterhead</title>
<link rel="stylesheet" href="https://fonts.googleapis.com/css2?family=Open+Sans:wght@400;600;700&display=swap">
<style>
  :root {
    --backdrop: #ececec;
    --paper: #f7f7f6;
    --ink: #4a4a4a;
    --ink-soft: #6a6a6a;
    --charcoal: #454547;
    --amber: #d98b25;
    --white: #ffffff;
  }
  * { box-sizing: border-box; margin: 0; padding: 0; }
  html, body {
    width: 1200px; height: 795px; overflow: hidden;
    background: var(--backdrop);
    font-family: "Open Sans", Arial, sans-serif;
  }
  .letterhead {
    position: absolute; left: 330px; top: 16px;
    width: 540px; height: 763px;
    background: var(--paper);
    box-shadow: 0 2px 10px rgba(0,0,0,.12);
    overflow: hidden;
    color: var(--ink);
  }
  .brand {
    position: absolute; top: 46px; left: 0; right: 0;
    text-align: center;
    font-size: 20px; font-weight: 400; letter-spacing: .5px;
    color: var(--amber);
  }
  .contact {
    position: absolute; top: 108px; left: 50px;
    font-style: normal;
    font-size: 9px; line-height: 12px; color: var(--ink);
  }
  .contact-phone { display: flex; align-items: center; gap: 4px; font-weight: 700; }
  .contact-phone svg { width: 8px; height: 8px; fill: var(--amber); }
  .contact-line { padding-left: 12px; }
  .letter {
    position: absolute; top: 190px; left: 96px; width: 360px;
    font-size: 8.6px; line-height: 13px; color: var(--ink-soft);
  }
  .letter p { margin-bottom: 13px; }
  .letter .salutation { margin-bottom: 12px; }
  .letter .closing { margin-top: 20px; margin-bottom: 6px; }
  .signature {
    display: block; width: 130px; height: 26px;
    border-radius: 3px;
    background: linear-gradient(90deg, #d9d9d9, #ececec);
  }
  .footer-swoosh { position: absolute; left: 0; bottom: 0; width: 540px; height: 400px; }
  .website {
    position: absolute; right: 42px; bottom: 28px;
    font-size: 10px; color: var(--white); letter-spacing: .3px;
  }
  .website strong { font-weight: 700; }
</style>
</head>
<body>
  <main class="letterhead">
    <div class="brand">Sterling Floorworks</div>

    <address class="contact">
      <div class="contact-phone">
        <svg viewBox="0 0 10 10" aria-hidden="true"><path d="M2 0.5l2 2-1 1.2c.6 1.3 1.6 2.3 2.9 2.9l1.2-1 2 2-1.3 1.8C4.6 9.2.8 5.4.2 1.8z"/></svg>
        <span>941.382.5519</span>
      </div>
      <div class="contact-line">5127 W. Harbor Lane</div>
      <div class="contact-line">Brookfield OR 97381</div>
    </address>

    <section class="letter">
      <p class="salutation">Dear Dana Whitfield,</p>
      <p>Lorem ipsum dolor sit amet, consectetuer adipiscing elit, sed diam nonummy nibh euismod tincidunt ut laoreet dolore magna aliquam erat volutpat. Ut wisi enim ad minim veniam, quis nostrud exerci tation ullamcorper suscipit lobortis nisl ut aliquip ex ea commodo consequat. Duis dolore te feugait nulla facilisi. Nam liber tempor cum soluta nobis eleifend option congue nihil imperdiet doming id quod mazim placerat facer possim assum. Lorem ipsum dolor sit amet, consectetuer adipiscing elit, sed diam nonummy nibh euismod tincidunt ut laoreet dolore magna aliquam erat volutpat. Ut wisi enim ad minim veniam, quis nostrud exerci tation ullamcorper suscipit lobortis nisl ut aliquip ex ea commodo consequat.</p>
      <p>Consectetuer adipiscing elit, sed diam nonummy nibh euismod tincidunt ut laoreet dolore magna aliquam erat volutpat. Ut wisi enim ad minim veniam, quis nostrud exerci tation ullamcorper suscipit lobortis nisl ut aliquip ex ea commodo consequat. Consectetuer adipiscing elit, sed diam nonummy nibh euismod tincidunt ut laoreet dolore magna aliquam erat volutpat. Ut wisi enim ad minim veniam, quis nostrud exerci tation ullamcorper suscipit lobortis nisl ut aliquip ex ea commodo consequat.</p>
      <p>Consectetuer adipiscing elit, sed diam nonummy nibh euismod tincidunt ut laoreet dolore magna aliquam erat volutpat. Ut wisi enim ad minim veniam, quis nostrud exerci tation ullamcorper suscipit lobortis nisl ut aliquip ex ea commodo consequat. Consectetuer adipiscing elit, sed diam nonummy nibh euismod tincidunt ut laoreet dolore magna aliquam erat volutpat. Ut wisi enim ad minim veniam, quis nostrud exerci tation ullamcorper suscipit lobortis nisl ut aliquip ex ea commodo consequat.</p>
      <p class="closing">Sincerely Yours</p>
      <span class="signature" role="img" aria-label="Handwritten signature of Marcus Ellery"></span>
    </section>

    <svg class="footer-swoosh" viewBox="0 0 540 400" preserveAspectRatio="none" aria-hidden="true">
      <path d="M210 400 C330 330 450 260 540 110 L540 400 Z" fill="var(--charcoal)"/>
      <path d="M200 362 C340 330 460 220 540 0 L540 10 C465 225 345 335 200 364 Z" fill="var(--amber)"/>
    </svg>

    <div class="website">www.<strong>sterlingfloorworks</strong>.com</div>
  </main>
</body>
</html>
```